Glass window Vinyl

We are in need of window vinyls for the building shown in the photos. The current vinyls will come down, and we will install the new signage created by this process. We need to advertise:

"Harwell's Landing Pop Up Market"

Then, below that, it should say for rental inquiries call : 555.613.0872 with our logo which is attached along with our colors and brand guidelines. You may add more color to the Harwells landing pop up market signage if appropriate. It should be large enough to be easily read from the road by those passing by.

```html
<!DOCTYPE html>
<html lang="en">
<head>
<meta charset="utf-8">
<title>Harwell's Landing Pop Up Market – Window Vinyl</title>
<link rel="stylesheet" href="https://fonts.googleapis.com/css2?family=Lato:wght@400;700&family=Josefin+Sans:wght@400&display=swap">
<style>
  :root {
    --backdrop: #4a4a4a;
    --navy: #213f4c;
    --gold: #b9a272;
    --white: #ffffff;
    --photo-light: #e9ebed;
    --photo-mid: #b9bec3;
    --photo-dark: #8d949a;
  }
  * { margin: 0; padding: 0; box-sizing: border-box; }
  html, body {
    width: 1200px; height: 1200px; overflow: hidden;
    background: var(--backdrop);
  }
  .vinyl {
    position: absolute; left: 133px; top: 133px;
    width: 934px; height: 934px;
    background: var(--navy);
  }
  .storefront-photo {
    position: absolute; left: 0; top: 0; width: 934px; height: 335px;
    background: linear-gradient(180deg, var(--photo-light) 0%, var(--photo-mid) 55%, var(--photo-dark) 100%);
  }
  .brand-block {
    position: absolute; left: 290px; top: 0; width: 354px; height: 173px;
    background: var(--navy);
    display: flex; flex-direction: column; align-items: center; justify-content: center;
    gap: 14px;
  }
  .brand-mark { width: 18px; height: 18px; background: var(--gold); }
  .brand-name {
    font-family: "Lato", sans-serif; font-weight: 400;
    font-size: 22px; letter-spacing: 4px; color: var(--white);
  }
  .title-band {
    position: absolute; left: 0; top: 335px; width: 934px; height: 185px;
    background: var(--gold);
    display: flex; flex-direction: column; align-items: center; justify-content: center;
  }
  .market-title {
    font-family: "Lato", sans-serif; font-weight: 400;
    font-size: 76px; line-height: 82px; color: var(--navy);
    text-align: center; text-transform: uppercase;
  }
  .contact-panel {
    position: absolute; left: 56px; top: 520px; width: 822px;
  }
  .contact-label {
    margin-top: 36px;
    font-family: "Lato", sans-serif; font-weight: 400;
    font-size: 58px; line-height: 60px; color: var(--gold);
    text-align: center; white-space: nowrap;
  }
  .rule { height: 4px; background: var(--gold); }
  .rule-top { margin-top: 16px; }
  .phone-number {
    font-family: "Josefin Sans", sans-serif; font-weight: 400;
    font-size: 168px; line-height: 200px; letter-spacing: -6px;
    color: var(--gold); text-align: center; white-space: nowrap;
    padding-top: 10px;
  }
</style>
</head>
<body>
  <div class="vinyl">
    <div class="storefront-photo" role="img" aria-label="Photo of the storefront building with grey siding, white trim and rental posters in the windows"></div>
    <div class="brand-block">
      <span class="brand-mark"></span>
      <span class="brand-name">HARWELL GROVE PROPERTIES</span>
    </div>
    <div class="title-band">
      <h1 class="market-title">Harwell's Landing<br>Pop Up Market</h1>
    </div>
    <div class="contact-panel">
      <p class="contact-label">FOR RENTAL INQUIRIES CALL:</p>
      <div class="rule rule-top"></div>
      <p class="phone-number">555.613.0872</p>
      <div class="rule"></div>
    </div>
  </div>
</body>
</html>
```